Einladungskarte
Zielgruppe
Hochzeitsgäste zwischen 30 und 40
Aufgabenstellung
Die Einladung hat folgende Eckdaten:
- Format Din A5 (Doppelseitiger DinA 4 gefalzt) Einladungsbogen (wird leichter Karton)
- Zusätzlicher Einlagebogen für Einladungstext
- Stil klassisch/elegant eher schlicht aber jung
- Grundthema Gerberablume (weiß, beige, rot oder orange)
- Hintergrund (hell)
- Zusätzlich zur Einladung wird Bildrecht der Blume für ein Banner auf der Hochzeitswebseite benötigt
- Editierbare Graphikdatei wird benötigt (da der Text der Einladung noch nicht final ist)

```html
<!DOCTYPE html>
<html lang="de">
<head>
<meta charset="utf-8">
<title>Einladung zur Hochzeit</title>
<link rel="stylesheet" href="https://fonts.googleapis.com/css2?family=Questrial&display=swap">
<style>
  :root {
    --page-bg: #f4f2ef;
    --card-white: #ffffff;
    --text-dark: #1c1c1c;
    --accent-orange: #d25a1a;
    --petal-orange: #e8771f;
    --petal-yellow: #f2a93a;
    --stem-green: #8d9b4a;
  }
  html, body {
    margin: 0;
    padding: 0;
    width: 1200px;
    height: 845px;
    overflow: hidden;
    background: var(--page-bg);
  }
  .canvas {
    position: relative;
    width: 1200px;
    height: 845px;
  }
  .invitation-card {
    position: absolute;
    left: 332px;
    top: 42px;
    width: 537px;
    height: 760px;
    background: var(--card-white);
    display: flex;
    flex-direction: column;
  }
  .flower-visual {
    width: 100%;
    height: 502px;
    background:
      radial-gradient(ellipse 48% 30% at 22% 45%, var(--petal-orange) 0%, var(--petal-yellow) 45%, rgba(242,169,58,0) 100%),
      radial-gradient(ellipse 40% 35% at 80% 70%, rgba(141,155,74,0.55) 0%, rgba(141,155,74,0) 100%),
      linear-gradient(180deg, #fbfaf7 0%, #f5f3ee 100%);
  }
  .invitation-text {
    flex: 1;
    display: flex;
    flex-direction: column;
    align-items: center;
    padding-top: 20px;
    font-family: "Questrial", sans-serif;
    font-size: 29px;
    line-height: 36px;
    letter-spacing: 0.5px;
    color: var(--text-dark);
    text-align: center;
  }
  .invitation-text .couple {
    color: var(--accent-orange);
  }
  .footer-band {
    height: 21px;
    background: var(--accent-orange);
  }
</style>
</head>
<body>
  <div class="canvas">
    <article class="invitation-card">
      <div class="flower-visual" role="img" aria-label="Nahaufnahme einer orangefarbenen Gerbera mit feinen Gräsern vor hellem Hintergrund"></div>
      <div class="invitation-text">
        <span>Einladung zur</span>
        <span>Hochzeit von</span>
        <span class="couple">Mareike &amp; Jonas</span>
      </div>
      <div class="footer-band"></div>
    </article>
  </div>
</body>
</html>
```